Brenmoor Group needs a business card

I would like the card to be simple but modern and elegant.
I like black and white.
or black and gold.
we are a private finance lender and also are involved in property and property developments.

please look at the business card photos i provided i would like B.G only one one side and all the other details on the other side use fonts that tie in with my theme.

Industry/Entity Type

Finance

Contact Information for Business Card

Brenmoor Group (B.G) Callum Brenmoor M: 0418396152 E: callumbren@quivomail.com

Font styles to use
Other font styles liked:
• Use fonts that would reflect our business

Colors
000000
ffffff

Requirements
Must have
• one side of details
• other side has either B.G or Brenmoor Group like in the photos provided

```html
<!DOCTYPE html>
<html lang="en">
<head>
<meta charset="utf-8">
<title>Brenmoor Group — Business Card</title>
<link rel="stylesheet" href="https://fonts.googleapis.com/css2?family=Fira+Sans:wght@300;400&display=swap">
<style>
  :root {
    --backdrop: #161616;
    --card-black: #232323;
    --gold: #c9a24a;
    --gold-light: #dcb862;
    --ink-dark: #2a2418;
    --card-w: 540px;
    --card-h: 309px;
  }
  * { box-sizing: border-box; margin: 0; padding: 0; }
  html, body {
    width: 1200px;
    height: 900px;
    overflow: hidden;
    background: var(--backdrop);
  }
  .canvas {
    width: 1200px;
    height: 900px;
    display: flex;
    align-items: center;
    justify-content: center;
    gap: 40px;
  }
  .card {
    position: relative;
    width: var(--card-w);
    height: var(--card-h);
    background: var(--card-black);
    box-shadow: 0 14px 40px rgba(0, 0, 0, 0.55);
    overflow: hidden;
  }

  /* Front side: name band */
  .name-band {
    position: absolute;
    left: 178px;
    right: 0;
    top: 156px;
    height: 62px;
    background: linear-gradient(100deg, var(--gold) 0%, var(--gold-light) 55%, var(--gold) 100%);
    display: flex;
    align-items: center;
    padding-left: 30px;
  }
  .name-band .company-name {
    font-family: "Fira Sans", sans-serif;
    font-weight: 300;
    font-size: 34px;
    letter-spacing: 0.5px;
    color: var(--ink-dark);
    white-space: nowrap;
  }

  /* Back side: details */
  .details-mark {
    position: absolute;
    left: 50px;
    top: 196px;
    width: 50px;
    height: 60px;
    background: var(--gold);
  }
  .details {
    position: absolute;
    left: 118px;
    top: 150px;
    list-style: none;
    font-family: "Fira Sans", sans-serif;
    font-weight: 400;
    font-size: 13px;
    line-height: 22px;
    letter-spacing: 1.3px;
    text-transform: uppercase;
    color: var(--gold);
  }
</style>
</head>
<body>
  <main class="canvas">
    <section class="card card-front" aria-label="Card front">
      <div class="name-band">
        <span class="company-name">Brenmoor Group</span>
      </div>
    </section>

    <section class="card card-back" aria-label="Card back">
      <div class="details-mark"></div>
      <ul class="details">
        <li class="details-name">Callum Brenmoor</li>
        <li class="details-phone">041 83 96 152</li>
        <li class="details-email">callumbren@quivomail.com</li>
        <li class="details-company">Brenmoor Group</li>
      </ul>
    </section>
  </main>
</body>
</html>
```